Career Development Program Flyer

Freshen up the look and make it more promotional. We want our teachers to know about the career tracks we offer. This document spells it all out, but we want it to pop! This will be a tool to help attract new applicants who are interested in future growth as well as retain our current staff who are interested in promotional opportunities.

Target Market(s)

our current teachers looking for growth or applicants interviewing who are interested in future growth with the company

Font styles to use
Serif
Sans Serif

Colors
3277b5
0255a3
cedeed
fbee3f
85acd3
fbf289

Requirements
Must have
• -our logo (i can send a new version if needed)
• -the information in the document provided
• -for more information on our company visit www.brightfernlearninghub.com

```html
<!DOCTYPE html>
<html lang="en">
<head>
<meta charset="utf-8">
<title>Career Growth Program</title>
<link rel="stylesheet" href="https://fonts.googleapis.com/css2?family=Cabin:wght@400;600;700&family=Lato:ital,wght@0,400;0,700;1,400&display=swap">
<style>
:root{
  --header-top:#1565b4;
  --header-bottom:#0b3f7e;
  --navy:#0b2140;
  --bright-blue:#1d72c2;
  --mid-blue:#0b4a8c;
  --yellow:#fbe33a;
  --yellow-deep:#f5c617;
  --orange:#eb9c10;
  --orange-dark:#a86a05;
  --mint:#eaf2dc;
  --mint-deep:#d6e6bd;
  --white:#ffffff;
  --ink:#0b2a52;
}
*{margin:0;padding:0;box-sizing:border-box}
html,body{width:1000px;height:1200px;overflow:hidden;background:#ffffff}
.flyer{position:relative;width:1000px;height:1200px;overflow:hidden;font-family:'Lato',sans-serif;color:var(--white);background:var(--navy)}
.header{position:absolute;left:0;top:0;width:1000px;height:132px;background:linear-gradient(180deg,var(--header-top),var(--header-bottom))}
.brand{position:absolute;left:40px;top:44px;display:flex;align-items:center;gap:14px}
.brand-dot{width:44px;height:44px;border-radius:50%;background:var(--yellow)}
.brand-name{font-family:'Cabin',sans-serif;font-weight:400;font-size:30px;color:var(--white)}
.main-office{position:absolute;right:34px;top:50px;text-align:right;font-family:'Cabin',sans-serif}
.main-office .label{font-size:21px}
.main-office .phone{font-size:26px;font-weight:700;display:flex;align-items:center;gap:6px;margin-top:2px}
.photo{position:absolute;left:0;top:132px;width:1000px;height:395px;background:linear-gradient(120deg,#c9a640 0%,#b77a9a 35%,#8c7fa8 60%,#9c8a7a 100%)}
.banner{position:absolute;left:0;top:438px;width:1000px;height:110px}
.banner-text{position:absolute;left:167px;top:438px;width:661px;height:89px;text-align:center;color:var(--ink)}
.banner-text h1{font-family:'Cabin',sans-serif;font-weight:700;font-size:48px;line-height:1;margin-top:12px}
.banner-text p{font-family:'Cabin',sans-serif;font-size:20px;margin-top:3px}
.teacher-col{position:absolute;left:0;top:527px;width:528px;height:581px;background:var(--navy)}
.teacher-title{position:absolute;left:31px;top:43px;width:461px;height:75px;background:var(--bright-blue);text-align:center;font-family:'Cabin',sans-serif;font-weight:700;font-size:28px;line-height:33px;padding-top:5px}
.role{position:absolute;left:52px;font-family:'Cabin',sans-serif;font-size:17px}
.role b{font-weight:700;font-size:19px}
.role::after{content:"";position:absolute;left:0;bottom:-6px;width:64px;height:2px;background:var(--white)}
.dots{position:absolute;left:30px;width:480px;list-style:none;font-size:13.5px;line-height:18px}
.dots li{position:relative;padding-left:24px;margin-bottom:6px}
.dots li::before{content:"";position:absolute;left:2px;top:4px;width:11px;height:11px;border-radius:50%;background:var(--white)}
.aide-col{position:absolute;left:528px;top:527px;width:472px;height:431px;background:linear-gradient(90deg,var(--mint-deep),var(--mint) 70%,#f3f7ec)}
.aide-title{position:absolute;left:80px;top:43px;font-family:'Cabin',sans-serif;font-weight:700;font-size:23px;line-height:27px;color:var(--ink)}
.aide-title span{text-decoration:underline;text-underline-offset:4px}
.aide-bar{position:absolute;left:0;height:32px;background:var(--mid-blue);clip-path:polygon(0 0,92% 0,100% 100%,0 100%);font-family:'Cabin',sans-serif;font-weight:700;font-size:17.5px;line-height:32px;padding-left:32px}
.aide-bar small{font-size:11px;font-style:italic;font-weight:400}
.diamonds{position:absolute;left:50px;list-style:none;color:var(--ink);font-family:'Cabin',sans-serif;font-size:17px;line-height:23px}
.diamonds li{position:relative;padding-left:30px}
.diamonds li::before{content:"";position:absolute;left:3px;top:7px;width:10px;height:10px;background:var(--ink);transform:rotate(45deg)}
.admin{position:absolute;left:528px;top:958px;width:472px;height:150px;background:var(--mid-blue)}
.admin h2{position:absolute;left:44px;top:12px;font-family:'Cabin',sans-serif;font-weight:700;font-size:22px}
.admin .note{position:absolute;left:44px;top:40px;font-size:10px;font-style:italic;padding-bottom:3px;border-bottom:1px solid var(--white)}
.admin ul{position:absolute;list-style:none;font-family:'Cabin',sans-serif;font-size:16.5px;line-height:26px}
.admin li{position:relative;padding-left:24px}
.admin li::before{content:"";position:absolute;left:3px;top:10px;width:7px;height:7px;background:var(--white);transform:rotate(45deg)}
.admin .foot-note{position:absolute;left:44px;top:130px;font-size:10px;font-style:italic}
.footer{position:absolute;left:0;top:1108px;width:1000px;height:92px;background:linear-gradient(90deg,#0a3a78,var(--bright-blue) 55%,#0a3f80)}
.address{position:absolute;left:32px;top:24px;display:flex;gap:10px;font-family:'Cabin',sans-serif;font-size:18px;line-height:22px}
.more-info{position:absolute;right:30px;top:20px;text-align:center;font-family:'Cabin',sans-serif}
.more-info .label{font-size:21px}
.more-info .site{font-size:16px;display:flex;align-items:center;gap:6px;margin-top:2px}
</style>
</head>
<body>
<main class="flyer">
  <header class="header">
    <div class="brand"><span class="brand-dot"></span><span class="brand-name">Bright Fern Learning Hub</span></div>
    <div class="main-office">
      <div class="label">Main Office:</div>
      <div class="phone">
        <svg width="22" height="22" viewBox="0 0 24 24" fill="#fff" aria-hidden="true"><path d="M6.6 10.8a15 15 0 0 0 6.6 6.6l2.2-2.2a1 1 0 0 1 1-.25 11.4 11.4 0 0 0 3.6.57 1 1 0 0 1 1 1V20a1 1 0 0 1-1 1A17 17 0 0 1 3 4a1 1 0 0 1 1-1h3.5a1 1 0 0 1 1 1c0 1.25.2 2.45.57 3.57a1 1 0 0 1-.25 1z"/></svg>
        (408) 555-0192
      </div>
    </div>
  </header>

  <div class="photo" role="img" aria-label="Photo of smiling preschool children together beside a yellow playground slide"></div>

  <svg class="banner" viewBox="0 0 1000 110" aria-hidden="true">
    <defs><linearGradient id="ribbonFace" x1="0" y1="0" x2="0" y2="1"><stop offset="0" stop-color="#fff07a"/><stop offset="0.5" stop-color="#fbe33a"/><stop offset="1" stop-color="#f5c617"/></linearGradient></defs>
    <polygon points="100,40 190,40 190,110 100,110 115,75" fill="#eb9c10"/>
    <polygon points="167,89 190,89 190,110" fill="#a86a05"/>
    <polygon points="900,40 810,40 810,110 900,110 885,75" fill="#eb9c10"/>
    <polygon points="833,89 810,89 810,110" fill="#a86a05"/>
    <rect x="167" y="0" width="666" height="89" fill="url(#ribbonFace)"/>
  </svg>
  <div class="banner-text">
    <h1>Career Growth Program</h1>
    <p>Qualifications by Position</p>
  </div>

  <section class="teacher-col">
    <h2 class="teacher-title">INFANT AND PRESCHOOL<br>TEACHER POSITIONS</h2>

    <div class="role" style="top:128px"><b>Infant or Preschool</b> Head Teacher, Jr. K Staff</div>
    <ul class="dots" style="top:163px">
      <li>Minimum to qualify: AA + 12 ECE units with 2 years' experience or 12 ECE units with 5 years' experience</li>
      <li>Professional, enthusiastic and an influential role model to their peers, specifically those teaching in their age group.</li>
    </ul>

    <div class="role" style="top:244px"><b>Infant or Preschool</b> Assistant Teacher</div>
    <ul class="dots" style="top:281px">
      <li>Entry level teachers</li>
      <li>12 ECE units minimum</li>
    </ul>

    <div class="role" style="top:331px"><b>Infant or Preschool</b> Master ECE Teacher</div>
    <ul class="dots" style="top:367px">
      <li>Minimum to qualify: B.A. Degree in Child Development with 2 years' experience or B.A. Degree in any subject with 12 ECE units and 7+ years' experience</li>
      <li>Minimum to qualify: B.A. Degree in Child Development with 2 years' experience or B.A. Degree in any subject with 12 ECE units and 7+ years' experience</li>
    </ul>

    <div class="role" style="top:482px"><b>Infant or Preschool</b> Assistant Teacher</div>
    <ul class="dots" style="top:519px">
      <li>Entry level teachers</li>
      <li>12 ECE units minimum</li>
    </ul>
  </section>

  <section class="aide-col">
    <h2 class="aide-title">INFANT AND PRESCHOOL<br><span>AIDE POSITIONS</span></h2>

    <div class="aide-bar" style="top:106px;width:300px">Infant or Preschool-Aide I</div>
    <ul class="diamonds" style="top:150px">
      <li>No ECE units</li><li>Limited experience</li><li>Training needed</li>
    </ul>

    <div class="aide-bar" style="top:216px;width:300px">Infant or Preschool-Aide II</div>
    <ul class="diamonds" style="top:262px;line-height:25px">
      <li>0-11 ECE units</li><li>Experience in the field</li>
    </ul>

    <div class="aide-bar" style="top:310px;width:380px">Infant or Preschool-Aide III, <small>Extended Day Staff</small></div>
    <ul class="diamonds" style="top:360px">
      <li>0-11 ECE units</li><li>Manages the classroom independently.</li><li>At least 3 years' experience</li>
    </ul>
  </section>

  <section class="admin">
    <h2>Administration Positions</h2>
    <p class="note">Not all positions are applicable at every site</p>
    <ul style="left:44px;top:56px">
      <li>Office Assistant</li><li>Office Administrator</li><li>Assistant Director</li>
    </ul>
    <ul style="left:270px;top:56px;line-height:24px">
      <li>Director</li><li>Senior Director</li>
    </ul>
    <p class="foot-note">For a comprehensive list of job duties, please see the job descriptions.</p>
  </section>

  <footer class="footer">
    <div class="address">
      <svg width="24" height="30" viewBox="0 0 24 30" aria-hidden="true"><path d="M12 1a9 9 0 0 0-9 9c0 7 9 16 9 16s9-9 9-16a9 9 0 0 0-9-9z" fill="#fff"/><circle cx="12" cy="10" r="3.5" fill="#0a3a78"/><ellipse cx="12" cy="28" rx="8" ry="1.6" fill="none" stroke="#fff" stroke-width="1.4"/></svg>
      <div>1480 Willowcrest Avenue, Building D<br>San Jose, CA 95130</div>
    </div>
    <div class="more-info">
      <div class="label">For More Info:</div>
      <div class="site">
        <svg width="15" height="15" viewBox="0 0 16 16" fill="none" stroke="#fff" stroke-width="1.2" aria-hidden="true"><circle cx="8" cy="8" r="6.5"/><ellipse cx="8" cy="8" rx="3" ry="6.5"/><path d="M1.5 8h13M2.5 4.8h11M2.5 11.2h11"/></svg>
        www.brightfernlearninghub.com
      </div>
    </div>
  </footer>
</main>
</body>
</html>
```